Cover Page for Pagewell, CareerLoop & Dwellfind.com

I'm needing a cover page for Pagewell, CareerLoop & Dwellfind.com. I already have my logo and some samples of what I'm looking for but open to new ideals. I'm in the real estate business and want something that looks very professional and clean. The area I cover is located in the Lake Norman area of North Carolina so would like to incorporate a lake background along with my logo, headshot and contact information.

```html
<!DOCTYPE html>
<html lang="en">
<head>
<meta charset="utf-8">
<title>Mark Hadley – Broker | Realtor Cover</title>
<link href="https://fonts.googleapis.com/css2?family=Montserrat:wght@600&family=Poppins:wght@500;600;700&display=swap" rel="stylesheet">
<style>
  :root {
    --lake-light: #4aa585;
    --lake-mid: #2f8d6c;
    --lake-deep: #1f7a58;
    --shore: #17603f;
    --white: #ffffff;
    --brand-green: #0f8a4f;
    --phone-green: #0d7a45;
    --name-gray: #5f6368;
    --suit-light: #4a5f86;
    --suit-dark: #263654;
  }
  html, body { margin: 0; padding: 0; overflow: hidden; }
  body { width: 1200px; height: 381px; background: var(--white); }
  .cover {
    position: relative; width: 1200px; height: 381px; overflow: hidden;
    font-family: "Poppins", sans-serif; color: var(--white);
  }
  .lake-scene {
    position: absolute; inset: 0;
    background:
      radial-gradient(ellipse 120px 60px at 655px 120px, rgba(190,240,200,.45), transparent 70%),
      linear-gradient(180deg, transparent 0 150px, var(--shore) 160px 178px, transparent 186px),
      linear-gradient(180deg, var(--lake-light) 0%, var(--lake-mid) 45%, var(--lake-deep) 100%);
  }
  .shapes { position: absolute; inset: 0; }
  .brand {
    position: absolute; left: 74px; top: 0; width: 324px; text-align: center;
  }
  .brand-square {
    width: 28px; height: 28px; background: var(--brand-green);
    margin: 34px auto 0;
  }
  .brand-name {
    font-family: "Montserrat", sans-serif; font-weight: 600;
    font-size: 23px; letter-spacing: .5px; color: var(--name-gray);
    margin-top: 14px; line-height: 1;
  }
  .brand-title {
    font-family: "Montserrat", sans-serif; font-weight: 600;
    font-size: 7.5px; letter-spacing: 2.6px; color: var(--name-gray);
    margin-top: 5px;
  }
  .contact {
    position: absolute; left: 500px; width: 314px; top: 124px; text-align: center;
  }
  .contact-lead { font-size: 24px; font-weight: 600; line-height: 1; }
  .contact-phone {
    display: inline-block; margin-top: 8px; padding: 0 13px;
    height: 37px; line-height: 38px; border-radius: 18px;
    background: var(--white); color: var(--phone-green);
    font-weight: 700; font-size: 18.5px; letter-spacing: .3px;
  }
  .contact-line { font-size: 17px; font-weight: 500; line-height: 26px; }
  .contact-web { margin-top: 6px; }
  .headshot {
    position: absolute; left: 812px; top: 31px; width: 388px; height: 350px;
    border-radius: 170px 170px 0 0;
    background: linear-gradient(180deg, var(--suit-light), var(--suit-dark));
  }
  .badge {
    position: absolute; top: 293px; height: 62px; border-radius: 6px;
    background: rgba(255,255,255,.82);
  }
  .badge-luxury { left: 83px; width: 177px; }
  .badge-leading { left: 282px; width: 242px; }
  .badge-divider {
    position: absolute; left: 271px; top: 298px; width: 1.5px; height: 52px;
    background: var(--white);
  }
</style>
</head>
<body>
<main class="cover">
  <div class="lake-scene" role="img" aria-label="Calm green-tinted lake at sunset with a wooded shoreline"></div>

  <svg class="shapes" width="1200" height="381" viewBox="0 0 1200 381" aria-hidden="true">
    <rect class="frame" x="17.5" y="14.5" width="1165" height="352" fill="none" stroke="#ffffff" stroke-width="1.5"/>
    <polygon class="brand-plate" points="98,0 376,0 398,81 237,199 74,83" fill="#ffffff"/>
    <polygon class="diagonal-band" points="660,381 1169,0 1200,0 1200,224 1020,381" fill="#ffffff"/>
    <line class="frame-return" x1="1183" y1="236" x2="1183" y2="367" stroke="#ffffff" stroke-width="1.5"/>
  </svg>

  <div class="brand">
    <div class="brand-square"></div>
    <div class="brand-name">MARK HADLEY</div>
    <div class="brand-title">BROKER | REALTOR</div>
  </div>

  <section class="contact">
    <div class="contact-lead">Call On</div>
    <div class="contact-phone">555-014-2290</div>
    <div class="contact-line contact-web">markhadleyhomes.com</div>
    <div class="contact-line">mark@harborpointrealty.com</div>
  </section>

  <div class="badge badge-luxury"></div>
  <div class="badge-divider"></div>
  <div class="badge badge-leading"></div>

  <div class="headshot" role="img" aria-label="Headshot of the broker in a blue plaid blazer and white shirt"></div>
</main>
</body>
</html>
```